Interval Timer App

Need to have design for the attached wireframe. Similar app can be found here: https://shop.velmorix.net/market/apps/entry?ref=nx.brollwick.cyclecounter

```html
<!DOCTYPE html>
<html lang="en">
<head>
<meta charset="UTF-8">
<title>Interval Timer – Rest Time</title>
<link href="https://fonts.googleapis.com/css2?family=Open+Sans:wght@400;600;700&display=swap" rel="stylesheet">
<style>
  :root {
    --bg-top: #63eef8;
    --bg-bottom: #14c3f4;
    --accent: #1c7ce0;
    --accent-dark: #1769c9;
    --card: #ffffff;
    --ink: #333a40;
    --ink-soft: #3e454b;
    --track-light: #ffffff;
  }
  * { margin: 0; padding: 0; box-sizing: border-box; }
  html, body { width: 675px; height: 1200px; overflow: hidden; }
  body {
    position: relative;
    font-family: "Open Sans", Arial, sans-serif;
    background: linear-gradient(180deg, var(--bg-top) 0%, var(--bg-bottom) 100%);
  }
  .back-button {
    position: absolute;
    left: 28px;
    top: 36px;
    width: 34px;
    height: 40px;
  }
  .set-label {
    position: absolute;
    left: 0;
    width: 740px;
    top: 166px;
    text-align: center;
    font-size: 22px;
    font-weight: 600;
    color: #1d2a33;
    letter-spacing: 0.5px;
  }
  .progress {
    position: absolute;
    left: 196px;
    top: 204px;
    width: 284px;
    height: 24px;
  }
  .card {
    position: absolute;
    left: 29px;
    top: 281px;
    width: 617px;
    height: 637px;
    background: var(--card);
    border-radius: 18px;
  }
  .card-title {
    position: absolute;
    top: 50px;
    width: 100%;
    text-align: center;
    font-size: 40px;
    font-weight: 600;
    color: var(--ink);
  }
  .current-time {
    position: absolute;
    top: 118px;
    width: 100%;
    text-align: center;
    font-size: 88px;
    font-weight: 600;
    color: var(--accent);
    line-height: 1.1;
  }
  .rest-list { position: absolute; left: 21px; right: 21px; top: 244px; list-style: none; }
  .rest-row {
    display: flex;
    justify-content: space-between;
    align-items: center;
    height: 54px;
  }
  .rest-name { font-size: 31px; color: var(--ink-soft); }
  .rest-row:nth-child(2) .rest-name { padding-left: 3px; }
  .rest-duration { font-size: 24px; font-weight: 700; color: var(--accent); }
  .next-button {
    position: absolute;
    left: 187px;
    top: 533px;
    width: 243px;
    height: 73px;
    border: none;
    border-radius: 37px;
    background: var(--accent);
    color: #fff;
    font-family: "Open Sans", Arial, sans-serif;
    font-size: 26px;
    font-weight: 600;
    letter-spacing: 1px;
  }
</style>
</head>
<body>
  <svg class="back-button" viewBox="0 0 34 40" aria-label="Back">
    <polyline points="24,6 10,20 24,34" fill="none" stroke="var(--accent)" stroke-width="5" stroke-linecap="round" stroke-linejoin="round"/>
  </svg>

  <div class="set-label">SET 2</div>

  <svg class="progress" viewBox="0 0 284 24" aria-label="Set progress">
    <line x1="2" y1="12" x2="175" y2="12" stroke="var(--accent-dark)" stroke-width="5" stroke-linecap="round"/>
    <line x1="175" y1="12" x2="282" y2="12" stroke="var(--track-light)" stroke-width="5" stroke-linecap="round"/>
    <circle cx="175" cy="12" r="9" fill="#ffffff" stroke="var(--accent-dark)" stroke-width="4"/>
  </svg>

  <section class="card">
    <h1 class="card-title">Rest time</h1>
    <div class="current-time">1:05</div>
    <ul class="rest-list">
      <li class="rest-row"><span class="rest-name">Rest 1</span><span class="rest-duration">1:00</span></li>
      <li class="rest-row"><span class="rest-name">Rest 2</span><span class="rest-duration">1:05</span></li>
    </ul>
    <button class="next-button">NEXT</button>
  </section>
</body>
</html>
```